Calvin Pruett Insurance Biz Card
Biz card and stationary
Calvin Pruett Insurance Biz Card - Financial Services
Creative Brief
Professional
Calvin Pruett
Independent Agent
Larkmoor, NC
pruettgroup@lanvex.example.net
www.calvinpruettinsurance.example.com
please use the logo we upload, and keep all font at a size 9 or 10.
please use the content we upload for an example of the back of the card

```html
<!DOCTYPE html>
<html lang="en">
<head>
<meta charset="utf-8">
<title>Calvin Pruett Insurance – Business Card</title>
<link rel="stylesheet" href="https://fonts.googleapis.com/css2?family=EB+Garamond:wght@400;600&display=swap">
<style>
  :root {
    --navy: #0f2557;
    --stone: #a9a8a0;
    --paper: #ffffff;
    --ink-light: #ffffff;
  }
  html, body {
    margin: 0;
    padding: 0;
    width: 1200px;
    height: 778px;
    overflow: hidden;
    background: var(--paper);
  }
  .card {
    position: relative;
    width: 1200px;
    height: 778px;
    background: var(--paper);
    font-family: "EB Garamond", Georgia, serif;
  }
  .card__wave {
    position: absolute;
    inset: 0;
    width: 1200px;
    height: 778px;
  }
  .brand {
    position: absolute;
    left: 60px;
    top: 300px;
    display: flex;
    align-items: center;
    gap: 22px;
  }
  .brand__square {
    width: 128px;
    height: 128px;
    background: var(--navy);
    flex: none;
  }
  .brand__name {
    color: var(--navy);
    font-weight: 600;
    font-size: 38px;
    line-height: 1.1;
    margin: 24px 0 0;
  }
  .contact {
    position: absolute;
    left: 710px;
    top: 190px;
    color: var(--ink-light);
  }
  .contact__name {
    margin: 0;
    font-size: 40px;
    font-weight: 600;
    line-height: 1.1;
  }
  .contact__title {
    margin: 8px 0 0;
    font-size: 28px;
    font-weight: 400;
    line-height: 1.2;
  }
  .contact__city {
    margin: 139px 0 22px;
    font-size: 25px;
    line-height: 1.2;
  }
  .contact__list {
    list-style: none;
    margin: 0;
    padding: 0;
    font-size: 24px;
    line-height: 41px;
  }
  .contact__list li {
    display: flex;
    align-items: center;
    gap: 10px;
    white-space: nowrap;
  }
  .contact__icon {
    width: 16px;
    height: 16px;
    flex: none;
  }
</style>
</head>
<body>
  <div class="card">
    <svg class="card__wave" viewBox="0 0 1200 778" aria-hidden="true">
      <path fill="var(--stone)" d="M560 0 C530 130 655 250 645 400 C635 560 575 650 588 778 L1200 778 L1200 0 Z"/>
      <path fill="var(--navy)" d="M598 0 C568 120 690 250 678 400 C666 560 598 645 606 778 L1200 778 L1200 0 Z"/>
    </svg>

    <div class="brand">
      <div class="brand__square"></div>
      <p class="brand__name">Calvin Pruett<br>Insurance, LLC</p>
    </div>

    <div class="contact">
      <h1 class="contact__name">Calvin Pruett</h1>
      <p class="contact__title">Independent Agent</p>
      <p class="contact__city">Larkmoor, NC</p>
      <ul class="contact__list">
        <li>
          <svg class="contact__icon" viewBox="0 0 16 16" aria-hidden="true"><path fill="currentColor" d="M3.5 1 L6 4 L4.8 5.8 C5.6 7.6 7.6 9.8 10 11 L11.8 9.8 L15 12.4 L13.4 15 C7 14.6 1.4 9 1 2.6 Z"/></svg>
          555-014-2093
        </li>
        <li>
          <svg class="contact__icon" viewBox="0 0 16 16" aria-hidden="true"><rect x="1" y="3" width="14" height="10" fill="none" stroke="currentColor" stroke-width="1.6"/><path d="M1 3 L8 9 L15 3" fill="none" stroke="currentColor" stroke-width="1.6"/></svg>
          pruettgroup@lanvex.example.net
        </li>
        <li>
          <svg class="contact__icon" viewBox="0 0 16 16" aria-hidden="true"><circle cx="8" cy="8" r="6.5" fill="none" stroke="currentColor" stroke-width="1.5"/><ellipse cx="8" cy="8" rx="2.8" ry="6.5" fill="none" stroke="currentColor" stroke-width="1.2"/><path d="M1.5 8 H14.5" stroke="currentColor" stroke-width="1.2"/></svg>
          www.calvinpruettinsurance.example.com
        </li>
      </ul>
    </div>
  </div>
</body>
</html>
```